Velvet Pressings Techno Label Business Card

I'm looking for a very clean business card for my Velvet Pressings music label. The label focusses on techno music. The card should include:

• my name : Bram Quintel as "Founder & CEO"
• email address: bram@velvet-pressings.example
• web: www.velvet-pressings.example
• facebook logo + /velvetpress
• twitter logo + /velvetpress
• soundcloud logo + /velvetpressings

Feel free to include your ideas! I'm looking forward to discuss about it.

Bram

Industry/Entity Type

Business

Contact Information for Business Card

I don't like glossy cards. Prefer matt.

Requirements
Nice to have
• Maybe on one side the complete logo, other side just the icon.
Should not have
• Flashy stuff. Must be clean and business like style.

```html
<!DOCTYPE html>
<html lang="en">
<head>
<meta charset="utf-8">
<title>Velvet Pressings – Business Card</title>
<link rel="stylesheet" href="https://fonts.googleapis.com/css2?family=Quicksand:wght@500;600;700&display=swap">
<style>
  :root {
    --page: #ffffff;
    --card-core: #1d1d1e;
    --card-edge: #080808;
    --accent: #f26522;
    --grey-light: #c9c9c9;
    --grey-mid: #9a9a9a;
    --divider: rgba(255, 255, 255, 0.07);
  }
  * { margin: 0; padding: 0; box-sizing: border-box; }
  html, body {
    width: 848px;
    height: 1200px;
    overflow: hidden;
    background: var(--page);
    font-family: "Quicksand", "Helvetica Neue", Arial, sans-serif;
  }
  .canvas { position: relative; width: 848px; height: 1200px; }

  .card {
    position: absolute;
    left: 0;
    width: 848px;
    height: 484px;
    overflow: hidden;
  }
  .card--front { top: 120px; }
  .card--back { top: 660px; }

  .card__texture {
    position: absolute;
    inset: 0;
    background: radial-gradient(ellipse 70% 80% at 50% 45%, var(--card-core) 0%, #121213 55%, var(--card-edge) 100%);
  }
  .card__divider {
    position: absolute;
    top: 0;
    bottom: 0;
    left: 433px;
    width: 1px;
    background: linear-gradient(to bottom, transparent, var(--divider) 30%, var(--divider) 70%, transparent);
  }

  /* Front */
  .brand {
    position: absolute;
    left: 56px;
    top: 142px;
    display: flex;
    align-items: center;
    gap: 26px;
  }
  .brand__mark {
    width: 46px;
    height: 46px;
    border-radius: 50%;
    background: var(--accent);
  }
  .brand__name {
    font-size: 62px;
    font-weight: 700;
    color: var(--accent);
    letter-spacing: -0.5px;
    line-height: 1;
  }
  .website {
    position: absolute;
    left: 0;
    right: 0;
    top: 330px;
    padding-left: 20px;
    text-align: center;
    font-size: 22px;
    font-weight: 500;
    letter-spacing: 1.5px;
    color: var(--grey-light);
  }

  /* Back */
  .back-brand {
    position: absolute;
    left: 440px;
    width: 336px;
    top: 92px;
    display: flex;
    justify-content: center;
    align-items: center;
    gap: 12px;
  }
  .back-brand__mark {
    width: 16px;
    height: 16px;
    border-radius: 50%;
    background: var(--accent);
  }
  .back-brand__name {
    font-size: 30px;
    font-weight: 700;
    color: var(--accent);
    line-height: 1;
  }
  .person {
    position: absolute;
    left: 440px;
    width: 336px;
    top: 188px;
    text-align: center;
  }
  .person__name {
    font-size: 44px;
    font-weight: 600;
    color: var(--grey-light);
    letter-spacing: 0.5px;
    line-height: 1.1;
  }
  .person__role {
    margin-top: 8px;
    font-size: 27px;
    font-weight: 500;
    color: var(--grey-mid);
    letter-spacing: 0.8px;
  }
  .contact {
    position: absolute;
    right: 432px;
    top: 196px;
    list-style: none;
  }
  .contact__item {
    display: flex;
    align-items: center;
    justify-content: flex-end;
    gap: 12px;
    height: 32px;
    font-size: 14.5px;
    font-weight: 500;
    color: var(--grey-light);
    letter-spacing: 0.3px;
  }
  .contact__icon { width: 18px; height: 18px; fill: var(--grey-light); flex: none; }
  .contact__square {
    width: 18px;
    display: flex;
    justify-content: center;
    flex: none;
  }
  .contact__square::before {
    content: "";
    width: 12px;
    height: 12px;
    background: var(--grey-mid);
  }
</style>
</head>
<body>
<main class="canvas">

  <section class="card card--front" aria-label="Card front">
    <div class="card__texture" role="img" aria-label="Dark charcoal surface with fine mesh texture"></div>
    <div class="card__divider"></div>
    <div class="brand">
      <span class="brand__mark"></span>
      <span class="brand__name">Velvet Pressings</span>
    </div>
    <p class="website">www.velvet-pressings.example</p>
  </section>

  <section class="card card--back" aria-label="Card back">
    <div class="card__texture" role="img" aria-label="Dark charcoal surface with fine mesh texture"></div>
    <div class="card__divider"></div>

    <div class="back-brand">
      <span class="back-brand__mark"></span>
      <span class="back-brand__name">Velvet Pressings</span>
    </div>

    <ul class="contact">
      <li class="contact__item">000 000 000
        <svg class="contact__icon" viewBox="0 0 24 24"><path d="M6.6 10.8a15.1 15.1 0 0 0 6.6 6.6l2.2-2.2c.3-.3.7-.4 1-.2 1.1.4 2.3.6 3.6.6.6 0 1 .4 1 1V20c0 .6-.4 1-1 1A17 17 0 0 1 3 4c0-.6.4-1 1-1h3.5c.6 0 1 .4 1 1 0 1.3.2 2.5.6 3.6.1.3 0 .7-.2 1z"/></svg>
      </li>
      <li class="contact__item">0000 First Street aaa aaa, CA 99000
        <svg class="contact__icon" viewBox="0 0 24 24"><path d="M12 2a7 7 0 0 0-7 7c0 5.2 7 13 7 13s7-7.8 7-13a7 7 0 0 0-7-7zm0 9.5a2.5 2.5 0 1 1 0-5 2.5 2.5 0 0 1 0 5z"/></svg>
      </li>
      <li class="contact__item">bram@velvet-pressings.example
        <svg class="contact__icon" viewBox="0 0 24 24"><path d="M2 5h20v14H2z" opacity=".9"/><path d="M2 5l10 8 10-8" fill="none" stroke="#151515" stroke-width="1.8"/></svg>
      </li>
      <li class="contact__item">/velvetpress<span class="contact__square"></span></li>
      <li class="contact__item">/velvetpress<span class="contact__square"></span></li>
      <li class="contact__item">/velvetpressings<span class="contact__square"></span></li>
    </ul>

    <div class="person">
      <h1 class="person__name">Bram Quintel</h1>
      <p class="person__role">Founder &amp; CEO</p>
    </div>
  </section>

</main>
</body>
</html>
```